May/June Newsletter

We require a newsletter with as much infographic as possible

Attached is our previous newsletter as an example.

ONLY USE THE DATA IN EPC CHALLENGES

Target Market(s)

property market

Requirements
Must have
• Company colours and logo from
www.verdanthaus.co.uk

be similar to our previous newsletter. copy attached.

must have a screenshot of VHConnect attached

```html
<!DOCTYPE html>
<html lang="en">
<head>
<meta charset="utf-8">
<title>Verdant Haus – Energy Performance Certificates Challenges</title>
<link rel="stylesheet" href="https://fonts.googleapis.com/css2?family=Montserrat:wght@400;600;700;800&family=Mulish:ital,wght@0,400;0,600;0,700;1,400&display=swap">
<style>
:root{
  --ink:#333333;
  --brand-green:#5cb531;
  --green-dark:#6aac2a;
  --green-body:#7cc52b;
  --cream:#fff5b0;
  --charcoal:#2f2f2f;
  --slate-top:#737b80;
  --slate-bottom:#5b6368;
  --gold-dark:#d7b400;
  --gold:#fcdc00;
  --teal-dark:#2ab2a3;
  --teal:#33c4b4;
  --mist:#ebebeb;
  --footer:#2d2d2d;
  --white:#ffffff;
}
*{box-sizing:border-box;margin:0;padding:0}
html,body{width:1200px;height:3607px;overflow:hidden}
body{font-family:"Mulish",sans-serif;color:var(--ink);background:var(--white)}

.masthead{height:168px;display:flex;flex-direction:column;align-items:center;justify-content:center;gap:6px}
.brand{display:flex;align-items:center;gap:14px}
.brand-dot{width:34px;height:34px;border-radius:50%;background:var(--brand-green)}
.brand-name{font-family:"Montserrat",sans-serif;font-weight:800;font-size:44px;letter-spacing:1px;color:var(--ink)}
.tagline{font-family:"Montserrat",sans-serif;font-size:16px;letter-spacing:5px;color:#9a9a9a}

.hero{height:264px;background:var(--cream);position:relative;padding:90px 0 0 84px}
.hero h1{position:relative;z-index:1;width:700px;font-family:"Montserrat",sans-serif;font-weight:800;font-size:48px;line-height:1.08;color:var(--brand-green);white-space:nowrap}
.hero h1 span{display:block;color:var(--ink);font-size:44px}
.hero-art{position:absolute;right:22px;top:22px;width:360px;height:232px;border-radius:8px;background:linear-gradient(180deg,#c7e27a,#8cc63f)}

.band{position:relative;font-family:"Montserrat",sans-serif;font-weight:800;color:var(--white);font-size:40px;letter-spacing:1px;padding-left:84px;display:flex;align-items:center}
.band::after{content:"";position:absolute;left:120px;bottom:-22px;border-left:20px solid transparent;border-right:20px solid transparent;border-top:22px solid var(--band-colour);z-index:2}

.april .band{--band-colour:var(--green-dark);background:var(--green-dark);height:125px}
.april .body{height:271px;background:var(--green-body);position:relative;padding:52px 360px 0 84px;color:var(--white);font-size:17.5px;line-height:1.45}
.april p+p{margin-top:22px}
.rating-art{position:absolute;right:28px;top:-38px;width:290px;height:274px;background:linear-gradient(160deg,#b7e06a,#8fcf3a);border:6px solid #a5d957}

.beyond .band{--band-colour:var(--charcoal);background:var(--charcoal);height:84px}
.beyond .body{height:571px;background:linear-gradient(180deg,var(--slate-top),var(--slate-bottom));position:relative;padding:58px 60px 0 84px;color:var(--white);font-size:17px;line-height:1.45}
.beyond .body p+p{margin-top:22px}
.beyond .definition{position:relative;z-index:1;width:620px;font-size:22px;line-height:1.38;margin-top:30px !important}
.beyond .definition em{font-style:italic}
.homes-art{position:absolute;right:0;bottom:0;width:480px;height:270px;background:linear-gradient(180deg,rgba(205,205,195,.35),rgba(140,185,80,.55))}

.ongoing .band{--band-colour:var(--gold-dark);background:var(--gold-dark);height:82px}
.ongoing .body{height:451px;background:var(--gold);padding:70px 84px 0 84px;font-size:17px;line-height:1.42}
.ongoing h3{font-family:"Montserrat",sans-serif;font-weight:700;font-size:22px;margin-top:26px}
.ongoing h3.small{font-size:18px;margin-top:30px}

.mapping .band{--band-colour:var(--teal-dark);background:var(--teal-dark);height:144px;padding-top:24px}
.mapping .body{height:545px;background:var(--teal);position:relative;padding:74px 0 0 94px;font-size:19px;line-height:1.4}
.mapping h4{font-family:"Montserrat",sans-serif;font-weight:700;font-size:24px;color:var(--ink)}
.mapping ul{list-style:none;color:#2f6b66;margin-bottom:40px}
.screen-shot{position:absolute;left:536px;top:90px;width:580px;height:314px;border-radius:4px;background:linear-gradient(180deg,#e9ecef 0 8%,#fafafa 8%);box-shadow:0 4px 10px rgba(0,0,0,.15)}

.promo{height:552px;background:var(--mist);text-align:center;padding-top:86px;font-size:24px;line-height:1.5;color:#444}
.promo .product{margin:80px auto 40px;display:flex;align-items:center;justify-content:center;gap:14px}
.product-dot{width:40px;height:40px;border-radius:50%;background:var(--brand-green)}
.product-name{font-family:"Montserrat",sans-serif;font-weight:800;font-size:60px;color:var(--ink)}
.promo p{width:980px;margin:0 auto}

.footer{height:350px;background:var(--footer);display:flex;flex-direction:column;align-items:center;padding-top:134px;gap:58px}
.social{display:flex;gap:50px}
.social span{width:36px;height:36px;border-radius:50%;background:var(--brand-green)}
.legal{font-family:"Montserrat",sans-serif;font-size:16px;color:#e6e6e6;letter-spacing:.5px}
</style>
</head>
<body>

<header class="masthead">
  <div class="brand"><span class="brand-dot"></span><span class="brand-name">VERDANT HAUS</span></div>
  <div class="tagline">LEADERS IN ENERGY EFFICIENCY</div>
</header>

<section class="hero">
  <h1>ENERGY PERFORMANCE<span>CERTIFICATES CHALLENGES</span></h1>
  <div class="hero-art" role="img" aria-label="Illustration of green trees beside a rolled certificate"></div>
</section>

<section class="april">
  <h2 class="band">APRIL 2023</h2>
  <div class="body">
    <p>From April 2023 existing MEES regulations will be extended to cover all non-domestic tenancies (already in place for domestic tenancies since 1st April 2020).</p>
    <p>MEES (Minimum Energy Efficiency Standard) regulations make it unlawful to agree a new lease on a property with an EPC rating below an E unless an exemption has been put in place on the PRS register.</p>
    <div class="rating-art" role="img" aria-label="Illustration of a yellow house marked E with a sales sign, labelled minimum rating"></div>
  </div>
</section>

<section class="beyond">
  <h2 class="band">BEYOND APRIL 2023</h2>
  <div class="body">
    <p>The UK Governments long term aim of having net zero carbon emissions by 2050 has several key dates before to make this achievable.</p>
    <p>Consultation process closed in January this year into the minimum energy standards for non domestic properties. The consultation process looked into the future trajectory of measures up to 2030, with one suggestion being for commercial properties to be of minimum band C or B.</p>
    <p>The Clean Growth Strategy is already in place to help as many domestic properties achieve band C by 2035.</p>
    <p class="definition">The definition <em>is</em> two-pronged. Firstly, during the construction process of an asset, the amount of carbon emissions produced should be zero, or negative through the use of offsets or the export of on-site renewable energy. Secondly, during the use of the building, the amount of carbon emissions produced from the building’s operational energy should also be zero or negative.</p>
    <div class="homes-art" role="img" aria-label="Photo of a row of model houses with one green house standing out"></div>
  </div>
</section>

<section class="ongoing">
  <h2 class="band">ONGOING</h2>
  <div class="body">
    <p>As part of companies overall commitment to EPC management, companies face the following challenges that need to be proactively managed</p>
    <h3>EPC EXPIRY DATES</h3>
    <p>As EPCs are only valid for 10 years, there is a requirement to ensure that EPC valid dates are managed and in date to ensure that transactions aren’t delayed due to have an expired EPC. It also important to ensure these are done in advance as there is sometimes changes in the rating due to more stricter controls being applied.</p>
    <h3>MANAGING LOW RATED PROPERTIES AND IMPROVEMENTS.</h3>
    <p>Where properties fail current MEES compliance (F&amp;G), these properties should be identified and managed to ensure that any upcoming PPM or retrofit works are taken into consideration and the impact on the EPC</p>
    <h3 class="small">LEASE END DATES</h3>
  </div>
</section>

<section class="mapping">
  <h2 class="band">EPC MAPPING AND MONITORING</h2>
  <div class="body">
    <h4>Managing</h4>
    <ul>
      <li>EPC expiry dates</li><li>Lease end dates</li><li>EPC ratings</li><li>Exemptions</li><li>EPC rating planning</li>
    </ul>
    <h4>This can be done by:-</h4>
    <ul>
      <li>Type of site</li><li>Age of site</li><li>Location</li><li>Region</li><li>Portfolio</li>
    </ul>
    <div class="screen-shot" role="img" aria-label="Screenshot of the VHConnect dashboard showing EPC rating tiles, a bar chart by rating and an expiry table"></div>
  </div>
</section>

<section class="promo">
  <p>Verdant Haus have developed a market leading EPC management tool to meet the current and ongoing EPC challenges faced in the property market.</p>
  <div class="product"><span class="product-dot"></span><span class="product-name">VHConnect</span></div>
  <p>We are currently offering free trials on VHConnect to demonstrate how we can assist to manage the above challenges.</p>
</section>

<footer class="footer">
  <div class="social" role="img" aria-label="Social media links"><span></span><span></span><span></span><span></span></div>
  <div class="legal">© VERDANT HAUS - 2020 - DON'T UNSUBSCRIBE</div>
</footer>

</body>
</html>
```